Gombrevo business card

Based on company logo and website given , to design a business card temple. Slogan "Your furry friends deserves the best"
Color style please refer to our website

```html
<!DOCTYPE html>
<html lang="en">
<head>
<meta charset="utf-8">
<title>Gombrevo business card</title>
<link rel="stylesheet" href="https://fonts.googleapis.com/css2?family=Roboto:wght@400;700;900&display=swap">
<style>
  :root {
    --brand-blue: #3d62ad;
    --brand-blue-light: #5a7ec4;
    --card-white: #f7f7f7;
    --ink: #1d1d1f;
    --page-bg: #e4e5e8;
  }
  * { box-sizing: border-box; margin: 0; padding: 0; }
  html, body { width: 1200px; height: 985px; overflow: hidden; }
  body {
    background: var(--page-bg);
    font-family: "Roboto", Arial, sans-serif;
    position: relative;
  }
  .card {
    position: absolute;
    left: 250px;
    width: 700px;
    height: 400px;
    border-radius: 4px;
    box-shadow: 0 6px 18px rgba(0,0,0,0.18);
    overflow: hidden;
  }
  /* Back side */
  .card-back {
    top: 70px;
    background: linear-gradient(160deg, var(--brand-blue) 0%, var(--brand-blue) 55%, var(--brand-blue-light) 100%);
    color: #fff;
    text-align: center;
  }
  .card-back .wordmark {
    margin-top: 40px;
    font-size: 58px;
    font-weight: 700;
    letter-spacing: 1px;
    color: #fff;
  }
  .hours-title {
    margin-top: 14px;
    font-size: 21px;
    font-weight: 900;
    letter-spacing: 1.5px;
  }
  .hours-list {
    list-style: none;
    width: 270px;
    margin: 8px auto 0;
    font-size: 16px;
    letter-spacing: 0.8px;
    line-height: 22px;
  }
  .hours-list li { display: flex; align-items: baseline; }
  .hours-list .leader {
    flex: 1;
    border-bottom: 2px dotted rgba(255,255,255,0.85);
    margin: 0 2px 5px;
  }
  .slogan {
    margin-top: 14px;
    font-size: 20px;
    font-weight: 700;
    letter-spacing: 1.2px;
  }
  /* Front side */
  .card-front {
    top: 515px;
    background: linear-gradient(180deg, #ffffff 0%, var(--card-white) 100%);
    color: var(--ink);
  }
  .card-front .wordmark {
    position: absolute;
    right: 48px;
    top: 58px;
    font-size: 82px;
    font-weight: 700;
    color: var(--brand-blue);
    letter-spacing: 1px;
  }
  .person { position: absolute; left: 48px; top: 150px; }
  .person-name { font-size: 24px; font-weight: 900; color: var(--brand-blue); letter-spacing: 0.5px; }
  .person-title { font-size: 16px; margin-top: 4px; letter-spacing: 0.5px; }
  .divider {
    position: absolute;
    left: 100px;
    right: 48px;
    top: 196px;
    border-top: 2px solid var(--brand-blue);
  }
  .contacts {
    position: absolute;
    left: 48px;
    top: 226px;
    list-style: none;
    font-size: 19px;
    letter-spacing: 0.8px;
    line-height: 32px;
  }
  .contacts li { display: flex; align-items: center; gap: 12px; }
  .contacts svg { width: 18px; height: 18px; fill: var(--brand-blue); flex: none; }
  .address {
    position: absolute;
    right: 48px;
    bottom: 40px;
    text-align: right;
    font-size: 19px;
    letter-spacing: 0.8px;
    line-height: 26px;
  }
  .address-company { font-weight: 900; color: var(--brand-blue); }
</style>
</head>
<body>

<section class="card card-back">
  <div class="wordmark">Gombrevo</div>
  <h2 class="hours-title">WORKING HOURS</h2>
  <ul class="hours-list">
    <li><span>Monday</span><span class="leader"></span><span>9 am - 5 pm</span></li>
    <li><span>Tuesday</span><span class="leader"></span><span>9 am - 5 pm</span></li>
    <li><span>Wednesday</span><span class="leader"></span><span>9 am - 5 pm</span></li>
    <li><span>Thursday</span><span class="leader"></span><span>9 am - 5 pm</span></li>
    <li><span>Friday</span><span class="leader"></span><span>9 am - 5 pm</span></li>
    <li><span>Saturday</span><span class="leader"></span><span>9 am - 5 pm</span></li>
    <li><span class="leader"></span><span>closed</span></li>
  </ul>
  <p class="slogan">"Your furry friends deserves the best"</p>
</section>

<section class="card card-front">
  <div class="wordmark">Gombrevo</div>
  <div class="person">
    <div class="person-name">Name</div>
    <div class="person-title">Title</div>
  </div>
  <div class="divider"></div>
  <ul class="contacts">
    <li>
      <svg viewBox="0 0 24 24" aria-hidden="true"><path d="M6.6 10.8a15.1 15.1 0 0 0 6.6 6.6l2.2-2.2a1 1 0 0 1 1-.25 11.4 11.4 0 0 0 3.6.57 1 1 0 0 1 1 1V20a1 1 0 0 1-1 1A17 17 0 0 1 3 4a1 1 0 0 1 1-1h3.5a1 1 0 0 1 1 1c0 1.25.2 2.45.57 3.57a1 1 0 0 1-.25 1z"/></svg>
      +61 3 5550 1942
    </li>
    <li>
      <svg viewBox="0 0 24 24" aria-hidden="true"><path d="M2 8c3-4 17-4 20 0l-1 3-4-1V8c-2-.7-6-.7-8 0v2l-4 1zM5 13h14l1 7H4z"/></svg>
      1800 555 014
    </li>
    <li>
      <svg viewBox="0 0 24 24" aria-hidden="true"><path d="M2 5h20v14H2zm2 2v.5l8 5.5 8-5.5V7z"/></svg>
      sales@gombrevo.com.au
    </li>
    <li>
      <svg viewBox="0 0 24 24" aria-hidden="true"><circle cx="12" cy="12" r="10"/></svg>
      www.gombrevo.com.au
    </li>
  </ul>
  <address class="address" style="font-style:normal">
    <div class="address-company">Gombrevo</div>
    <div>4/22 Farrow Street</div>
    <div>Glen Ashby Vic 3190</div>
  </address>
</section>

</body>
</html>
```